Flyer Design Project

We need a flyer design for our lock company called 'Harwell Bolts'. It will be an A5 flyer delivered to local households advertising the benefits of upgrading their existing door locks to higher security , insurance approved ones.
We have the basic text/layout details and are looking forward to receiving your designs to help in the first stage of our new advertising programme.

Target Market(s)

This flyer is intended for general households.
I will be printing the final flyer as double sided, so it can be the same both sides or different each side depending on layout/content etc. any ideas suggestions will be much appreciated.

Industry/Entity Type

Advertising

Requirements
Must have
• HEADING- Something along the lines of 'Security Update', 'Security News' etc.

1) Basic facts- Every 37 seconds a home somewhere in Britain is burgled. In 70% of these burglaries the offenders gain entry through a door.

SUB HEADING- Who has the keys to your home?

TEXT- Over the years keys are lost, lent, borrowed, duplicated or not even handed over from previous owners and/or tennants.
Not only does this make your home more likely to be burgled it may also mean that your insurance policy will not cover you. As part of your insurance requirements you must have approved locks fitted, if they are not this can invalidate your policy.
Upgrading your homes security by upgrading and ensuring your locks are approved is a simple, cost-effective way to ensure not only your homes security but also your peace of mind.
For a free, no-obligation quotation from your local specialists call Harwell Bolts on 01632 960418.

None of this text is essential but, i feel, gets the message across well. If you have other ideas then please feel free to use your own ideas.

At the bottom of the page in small lettering will be;

'Harwell Bolts' is a trading name of Harwell Gates ltd. registered company no. 7316952. VAT #.642 1938 57. 14 Mill Row, Ashcombe.

Our company uses red normally for our name etc. This is by no means a must have but may help, It would also be beneficial to have some photos etc. to help with the text. Any questions please ask.

Nice to have
• I look forward to receiving your ideas and interpretations, i hope this will lead to working with you on our other future projects.
Yours sincerely
Colin Marbury.

```html
<!DOCTYPE html>
<html lang="en">
<head>
<meta charset="utf-8">
<title>Harwell Bolts – Security Flyer</title>
<link rel="stylesheet" href="https://fonts.googleapis.com/css2?family=Lobster+Two:ital,wght@1,700&family=Lato:wght@400;700&display=swap">
<style>
  :root {
    --alert-red: #e3110f;
    --ink: #0c0c0c;
    --body-ink: #222222;
    --muted: #555555;
    --paper: #ffffff;
    --art-light: #f6f6f6;
    --art-mid: #d9d9d9;
  }
  html, body {
    margin: 0;
    padding: 0;
    width: 846px;
    height: 1200px;
    overflow: hidden;
    background: var(--paper);
  }
  .flyer {
    box-sizing: border-box;
    width: 846px;
    height: 1200px;
    padding: 22px 50px 0;
    overflow: hidden;
    background: var(--paper);
    font-family: 'Lobster Two', cursive;
    font-style: italic;
    font-weight: 700;
    text-align: center;
    color: var(--ink);
    position: relative;
  }
  .flyer p, .flyer h1, .flyer h2 { margin: 0; }
  .headline {
    font-size: 44px;
    font-weight: 700;
    color: var(--alert-red);
    line-height: 1.1;
  }
  .burglar-illustration {
    width: 290px;
    height: 300px;
    margin: 14px auto 0;
    background: radial-gradient(ellipse at 50% 50%, var(--art-mid) 0%, var(--art-light) 65%, var(--paper) 100%);
  }
  .prompt {
    margin-top: 14px !important;
    font-size: 38px;
    line-height: 1.15;
  }
  .fact-label {
    margin-top: 16px !important;
    font-size: 30px;
    color: var(--alert-red);
  }
  .fact-text {
    margin-top: 6px !important;
    font-size: 32px;
    line-height: 1.25;
  }
  .subheading {
    margin-top: 22px !important;
    font-size: 34px;
    font-weight: 700;
    color: var(--alert-red);
    line-height: 1.15;
  }
  .body-copy {
    margin-top: 12px;
    font-family: 'Lato', sans-serif;
    font-style: normal;
    font-weight: 400;
    font-size: 17px;
    line-height: 1.5;
    color: var(--body-ink);
  }
  .body-copy p + p { margin-top: 8px; }
  .call-to-action {
    margin-top: 20px !important;
    font-size: 36px;
    line-height: 1.2;
  }
  .brand-name, .phone-number { color: var(--alert-red); }
  .legal-footer {
    position: absolute;
    left: 50px;
    right: 50px;
    bottom: 22px;
    font-family: 'Lato', sans-serif;
    font-style: normal;
    font-weight: 400;
    font-size: 12px;
    line-height: 1.4;
    color: var(--muted);
  }
</style>
</head>
<body>
  <main class="flyer">
    <h1 class="headline">Hey! Your house is being burgled!!</h1>
    <div class="burglar-illustration" role="img" aria-label="Cartoon burglar in a striped jumper and beanie holding a crowbar and a swag bag"></div>
    <p class="prompt">If not, don’t wait for it to happen.</p>
    <p class="fact-label">Did you know?</p>
    <p class="fact-text">Every 37 seconds a home somewhere in Britain is burgled. In 70% of these burglaries the offenders gain entry through a door.</p>

    <h2 class="subheading">Who has the keys to your home?</h2>
    <div class="body-copy">
      <p>Over the years keys are lost, lent, borrowed, duplicated or not even handed over from previous owners and/or tenants.</p>
      <p>Not only does this make your home more likely to be burgled, it may also mean that your insurance policy will not cover you. As part of your insurance requirements you must have approved locks fitted; if they are not, this can invalidate your policy.</p>
      <p>Upgrading your home’s security by ensuring your locks are approved is a simple, cost-effective way to ensure not only your home’s security but also your peace of mind.</p>
    </div>

    <p class="call-to-action">For a free, no-obligation quotation call<br><span class="brand-name">Harwell Bolts</span> on <span class="phone-number">01632 960418</span></p>

    <p class="legal-footer">‘Harwell Bolts’ is a trading name of Harwell Gates ltd. Registered company no. 7316952. VAT #. 642 1938 57. 14 Mill Row, Ashcombe.</p>
  </main>
</body>
</html>
```